A label for a bottle of Gin that reflect the area in which it is made - Farrow

I have attached a couple of labels that we are not very happy with. We are looking for something that portrays a premium brand. The bottle is called Verbelle 700ml. and the image should be max 9cm by 7cm. For details on webpage - see notes at quellon.co.uk/farrow and quellon.co.uk/farrowgin. The website should just be a single homepage with a link to quellon.co.uk/farrowgin

The words "Small Batch Handmade Gin" could feature

Number of Pages Required

1 page

Requirements
Nice to have
• Gold or Silver that can add to overall quality feel of the label.
Should not have
• Transparent labels look great when back lit but tend to disappear when on a dark bar with other brighter bottles. Avoid transparency

```html
<!DOCTYPE html>
<html lang="en">
<head>
<meta charset="utf-8">
<title>Farrow Gin – Label Variations</title>
<link href="https://fonts.googleapis.com/css2?family=Cinzel:wght@400;600;700&display=swap" rel="stylesheet">
<style>
  :root {
    --backdrop: #a8a8a8;
    --label-edge: #d3d3d5;
    --paper: #f1f1f1;
    --map-light: #ececec;
    --map-mid: #d6d6d6;
    --map-rose: #e6d4d6;
    --crimson: #9a1424;
    --crimson-dark: #6e0d18;
    --ink: #1a1a1a;
    --silver-light: #e2e2e2;
    --silver-dark: #8c8c8c;
    --white: #ffffff;
  }
  * { box-sizing: border-box; margin: 0; padding: 0; }
  html, body {
    width: 1200px;
    height: 1014px;
    overflow: hidden;
    background: var(--backdrop);
    font-family: "Cinzel", Georgia, serif;
  }
  .label-range {
    position: absolute;
    left: 90px;
    top: 309px;
    display: flex;
    gap: 60px;
  }
  .label {
    width: 300px;
    height: 396px;
    background: var(--label-edge);
    padding: 10px;
  }
  .label-face {
    position: relative;
    width: 100%;
    height: 100%;
    background: var(--paper);
    overflow: hidden;
  }
  .map-area {
    position: absolute;
    inset: 0;
    background: linear-gradient(125deg, var(--map-light) 0%, var(--map-mid) 45%, var(--map-light) 70%, var(--map-mid) 100%);
  }
  .label--crimson-band .map-area {
    background: linear-gradient(125deg, var(--map-light) 0%, var(--map-rose) 45%, var(--map-light) 70%, var(--map-rose) 100%);
  }
  .inner-frame {
    position: absolute;
    inset: 4px;
    border: 2px solid var(--crimson);
  }
  .brand-block {
    position: absolute;
    top: 14px;
    left: 0;
    right: 0;
    text-align: center;
  }
  .brand-place {
    font-size: 15px;
    font-weight: 600;
    letter-spacing: 3px;
    color: var(--ink);
  }
  .brand-spirit {
    font-size: 64px;
    font-weight: 700;
    line-height: 1;
    margin-top: -2px;
    color: var(--crimson);
  }
  .maker-mark {
    position: absolute;
    top: 150px;
    left: 0;
    right: 0;
    display: flex;
    align-items: center;
    justify-content: center;
    gap: 8px;
    font-size: 20px;
    font-weight: 600;
    letter-spacing: 2px;
    color: var(--crimson);
  }
  .maker-mark .mark-square {
    width: 14px;
    height: 14px;
    background: var(--crimson);
  }
  .tagline {
    position: absolute;
    left: 4px;
    right: 4px;
    bottom: 8px;
    text-align: center;
    font-size: 11px;
    font-weight: 700;
    letter-spacing: 1.6px;
    line-height: 1.2;
    color: var(--ink);
  }
  .label--crimson-rule .tagline {
    border-top: 2px solid var(--crimson);
    padding-top: 4px;
  }
  .label--crimson-band .tagline {
    bottom: 4px;
    padding: 4px 0;
    color: var(--white);
    background: linear-gradient(90deg, var(--crimson-dark), var(--crimson), var(--crimson-dark));
  }
  .label--noir .inner-frame { display: none; }
  .noir-band {
    position: absolute;
    top: 0;
    left: 0;
    right: 0;
    height: 98px;
    background: var(--ink);
  }
  .label--noir .brand-place { color: var(--silver-light); }
  .label--noir .brand-spirit {
    color: var(--silver-dark);
    background: linear-gradient(180deg, var(--silver-light), var(--silver-dark));
    -webkit-background-clip: text;
    background-clip: text;
    -webkit-text-fill-color: transparent;
  }
  .label--noir .maker-mark { color: var(--ink); }
  .label--noir .maker-mark .mark-square { background: var(--ink); }
</style>
</head>
<body>
  <main class="label-range">

    <section class="label label--crimson-rule">
      <div class="label-face">
        <div class="map-area" role="img" aria-label="Antique engraved map of the Farrow peninsula coastline"></div>
        <div class="inner-frame"></div>
        <div class="brand-block">
          <p class="brand-place">Farrow</p>
          <p class="brand-spirit">GIN</p>
        </div>
        <div class="maker-mark"><span class="mark-square"></span>FARROW</div>
        <p class="tagline">SMALL BATCH<br>HANDMADE GIN</p>
      </div>
    </section>

    <section class="label label--crimson-band">
      <div class="label-face">
        <div class="map-area" role="img" aria-label="Antique engraved map of the Farrow peninsula coastline, rose tinted"></div>
        <div class="inner-frame"></div>
        <div class="brand-block">
          <p class="brand-place">Farrow</p>
          <p class="brand-spirit">GIN</p>
        </div>
        <div class="maker-mark"><span class="mark-square"></span>FARROW</div>
        <p class="tagline">SMALL BATCH<br>HANDMADE GIN</p>
      </div>
    </section>

    <section class="label label--noir">
      <div class="label-face">
        <div class="map-area" role="img" aria-label="Antique engraved map of the Farrow peninsula coastline"></div>
        <div class="noir-band"></div>
        <div class="inner-frame"></div>
        <div class="brand-block">
          <p class="brand-place">Farrow</p>
          <p class="brand-spirit">GIN</p>
        </div>
        <div class="maker-mark"><span class="mark-square"></span>FARROW</div>
        <p class="tagline">SMALL BATCH<br>HANDMADE GIN</p>
      </div>
    </section>

  </main>
</body>
</html>
```